Poster Required for Cafe to promote Catering

I would like a Poster made to advertise that our business does catering.
On the poster we would like it to say:

Did you know that Lantern Pantry does Catering?
We offer Breakfast, Lunch, Morning and Afternoon Tea Options
Come instore to enquire

At the bottom of the flyer, can you please put the contact details:
Phone 0472 918 604
Email mia@lanternpantrykitchen.com

Poster Size A3

I have attached our logo and menu's so you can get a feel for what we like.

Target Market(s)

Hospital Staff: Doctors, Nurses, Admin

Industry/Entity Type

Hospitality

Requirements
Nice to have
• Some pictures of catering. Eg. Gourmet Sandwiches, Sliders
• You could check our instagram page for ideas on what we do..
• @lntpantry_qld

```html
<!DOCTYPE html>
<html lang="en">
<head>
<meta charset="utf-8">
<title>Lantern Pantry Catering Poster</title>
<link href="https://fonts.googleapis.com/css2?family=Montserrat:wght@700;800&family=PT+Sans&family=Great+Vibes&family=Oswald:wght@300&display=swap" rel="stylesheet">
<style>
  :root{
    --stage:#1a1a1a;
    --wine-deep:#2a0a0c;
    --wine:#5a1114;
    --red-glow:#a81a20;
    --cream:#fbf3ae;
    --cream-text:#f6e7a3;
    --gold-line:#c9ad62;
    --red-type:#c1272d;
    --ink:#2a1b1b;
    --rule:#8c6f5a;
  }
  *{margin:0;padding:0;box-sizing:border-box}
  html,body{width:1200px;height:857px;overflow:hidden;background:var(--stage)}
  .poster{
    position:absolute;left:302px;top:8px;width:595px;height:840px;overflow:hidden;
    background:
      radial-gradient(ellipse 320px 300px at 470px 330px,var(--red-glow) 0%,rgba(168,26,32,0) 100%),
      linear-gradient(180deg,var(--wine-deep) 0%,var(--wine) 45%,var(--wine-deep) 100%);
  }
  .food-photo{
    position:absolute;left:0;top:340px;width:595px;height:500px;
    background:
      radial-gradient(ellipse 130px 90px at 460px 400px,#f4f1ee 0%,rgba(244,241,238,0) 100%),
      radial-gradient(ellipse 120px 80px at 160px 330px,#b4602d 0%,rgba(180,96,45,0) 100%),
      radial-gradient(ellipse 140px 90px at 470px 190px,#e8e4e0 0%,rgba(232,228,224,0) 100%),
      linear-gradient(180deg,rgba(90,17,20,0) 0%,#3b4a6a 35%,#26324a 70%,#1b2233 100%);
  }
  .frame{position:absolute;left:12px;top:10px;width:571px;height:818px;border:1px solid var(--gold-line)}
  .panel{position:absolute;left:53px;width:267px;background:var(--cream)}
  .panel--top{top:10px;height:430px}
  .panel--bottom{top:728px;height:100px}
  .brand{
    position:absolute;left:131px;top:48px;width:106px;height:106px;border-radius:50%;
    background:var(--ink);display:flex;align-items:center;justify-content:center;
    font-family:'PT Sans',sans-serif;font-size:14px;letter-spacing:1.5px;color:var(--cream);text-align:center;line-height:1.2;
  }
  .rule{position:absolute;left:69px;width:235px;height:1px;background:var(--rule)}
  .rule--top{top:181px}
  .rule--bottom{top:412px}
  .headline{
    position:absolute;left:53px;top:190px;width:267px;text-align:center;
    font-family:'Montserrat',sans-serif;font-weight:800;color:var(--red-type);line-height:1;
  }
  .headline span{display:block}
  .headline .l1{font-size:40px}
  .headline .l2{font-size:52px;margin-top:-2px}
  .headline .l3{font-size:23px;color:var(--ink);margin-top:2px}
  .headline .l4{font-size:40px;margin-top:1px}
  .headline .l5{font-size:32px;margin-top:1px}
  .headline .l6{font-size:31px;margin-top:1px}
  .offer{position:absolute;left:340px;top:60px;width:220px;text-align:center;color:var(--cream-text)}
  .offer svg{display:block;margin:0 auto}
  .offer__title{font-family:'Great Vibes',cursive;font-size:50px;line-height:1;margin:6px 0 2px}
  .offer__list{font-family:'PT Sans',sans-serif;font-size:19px;line-height:25px;margin-top:18px}
  .enquire{position:absolute;left:53px;top:687px;width:267px;text-align:center;font-family:'PT Sans',sans-serif;font-size:19px;color:var(--cream-text)}
  .phone{position:absolute;left:53px;top:744px;width:267px;text-align:center;font-family:'Oswald',sans-serif;font-weight:300;font-size:44px;line-height:1;color:var(--red-type)}
  .email{position:absolute;left:53px;top:800px;width:267px;text-align:center;font-family:'PT Sans',sans-serif;font-size:14px;color:var(--ink)}
</style>
</head>
<body>
<main class="poster">
  <div class="food-photo" role="img" aria-label="Photo of gourmet seeded-bun sliders with ham, cheese and lettuce, a bowl of salad and a cup of red tea with a napkin"></div>
  <div class="frame"></div>

  <div class="panel panel--top"></div>
  <div class="brand">LANTERN<br>PANTRY</div>
  <div class="rule rule--top"></div>
  <h1 class="headline">
    <span class="l1">DID YOU</span>
    <span class="l2">KNOW</span>
    <span class="l3">LANTERN PANTRY</span>
    <span class="l5">DOES</span>
    <span class="l6">CATERING?</span>
  </h1>
  <div class="rule rule--bottom"></div>

  <section class="offer">
    <svg width="160" height="24" viewBox="0 0 160 24" aria-hidden="true">
      <rect x="0" y="9" width="90" height="7" rx="3.5" fill="var(--cream-text)"/>
      <path d="M88 7 Q100 4 110 4 L160 4 L160 5.5 L112 5.5 L112 9 L160 9 L160 10.5 L112 10.5 L112 14 L160 14 L160 15.5 L112 15.5 L112 19 L160 19 L160 20.5 L110 20.5 Q100 20.5 88 18 Z" fill="var(--cream-text)"/>
    </svg>
    <div class="offer__title">We offer</div>
    <svg width="160" height="18" viewBox="0 0 160 18" aria-hidden="true">
      <rect x="0" y="5" width="62" height="8" rx="4" fill="var(--cream-text)"/>
      <path d="M60 4 L150 4 Q160 4 156 8 Q150 15 120 15 L60 14 Z" fill="var(--cream-text)"/>
    </svg>
    <p class="offer__list">Breakfast &nbsp;|&nbsp; Lunch<br>Morning &amp; Afternoon<br>Tea Options</p>
  </section>

  <p class="enquire">Come in store to enquire</p>
  <div class="panel panel--bottom"></div>
  <p class="phone">0472 918 604</p>
  <p class="email">mia@lanternpantrykitchen.com</p>
</main>
</body>
</html>
```